Meadow Spa & Sauna Digital Billboard

This is a digital billboard so we are looking for a fresh design that will capture people's attention. The current billboard is a simple black text "#SteamyNights" over a white background with a picture of an zelphone with one of our photos (Reference attached) We enjoy how clean and simple this design is, but open to other concepts. Since the weather is getting colder, a lot of people come to our spa because we offer various dry saunas and hot baths in addition to our spa services. We have a few photos for reference on our website information view www.meadowsteamhouse.com , but you can email me for additional photo content - gunther@meadowsteamhouse.com

Target Market(s)

New Jersey Locals

Colors
0255a3
ec1f27
f37122
ffc214

Requirements
Must have
• Font is "Barlow"
Nice to have
• #SteamyNights hashtag

```html
<!DOCTYPE html>
<html lang="en">
<head>
<meta charset="utf-8">
<title>Meadow Spa &amp; Sauna — Digital Billboard</title>
<link rel="stylesheet" href="https://fonts.googleapis.com/css2?family=Barlow:wght@300;500;700&display=swap">
<style>
  :root {
    --page-bg: #2b2b2b;
    --board-teal: #72ccd5;
    --ink-white: #ffffff;
    --warm-deep: #5a1e0c;
    --warm-mid: #b8541d;
    --warm-glow: #f0a04a;
  }
  html, body {
    margin: 0;
    width: 1200px;
    height: 880px;
    overflow: hidden;
    background: var(--page-bg);
  }
  .billboard {
    position: absolute;
    left: 20px;
    top: 271px;
    width: 1160px;
    height: 337px;
    display: block;
  }
  .board-field { fill: var(--board-teal); }
  .headline {
    font-family: "Barlow", sans-serif;
    font-size: 76px;
    fill: var(--ink-white);
  }
  .headline-light { font-weight: 300; }
  .headline-bold { font-weight: 700; }
  .photo-ring {
    fill: none;
    stroke: var(--ink-white);
    stroke-width: 1.6;
  }
  .brand-dot { fill: var(--ink-white); }
  .brand-name {
    font-family: "Barlow", sans-serif;
    font-weight: 500;
    fill: var(--ink-white);
  }
  .brand-name-main { font-size: 72px; letter-spacing: 2px; }
  .brand-name-sub { font-size: 17px; letter-spacing: 4px; }
</style>
</head>
<body>
<svg class="billboard" viewBox="0 0 1212 352" xmlns="http://www.w3.org/2000/svg" aria-label="Meadow Spa &amp; Sauna billboard">
  <defs>
    <clipPath id="board-edge"><rect width="1212" height="352"/></clipPath>
    <radialGradient id="sauna-warmth" cx="50%" cy="40%" r="60%">
      <stop offset="0" stop-color="var(--warm-glow)"/>
      <stop offset="0.55" stop-color="var(--warm-mid)"/>
      <stop offset="1" stop-color="var(--warm-deep)"/>
    </radialGradient>
  </defs>

  <rect class="board-field" width="1212" height="352"/>

  <text class="headline" x="60" y="100"><tspan class="headline-light">#steamy</tspan><tspan class="headline-bold">nights</tspan></text>

  <g class="photo-cluster" clip-path="url(#board-edge)">
    <path class="photo-ring" d="M 60 352 A 135 135 0 0 1 290 178"/>
    <path class="photo-ring" d="M 385 262 A 150 150 0 0 1 655 175"/>
    <path class="photo-ring" d="M 620 285 A 85 85 0 0 1 770 352"/>
    <path class="photo-ring" d="M 320 215 A 110 110 0 0 1 430 250"/>

    <circle cx="175" cy="283" r="115" fill="url(#sauna-warmth)" role="img" aria-label="Photo: guest relaxing by warm slatted sauna light"/>
    <circle cx="520" cy="265" r="125" fill="url(#sauna-warmth)" role="img" aria-label="Photo: guest seated before a glowing wooden sauna screen"/>
    <circle cx="348" cy="322" r="97" fill="url(#sauna-warmth)" role="img" aria-label="Photo: three friends sitting together in a wooden sauna room"/>
    <circle cx="691" cy="323" r="68" fill="url(#sauna-warmth)" role="img" aria-label="Photo: guest resting on the floor of a warm sauna room"/>
  </g>

  <g class="brand-lockup">
    <circle class="brand-dot" cx="955" cy="112" r="42"/>
    <text class="brand-name brand-name-main" x="955" y="272" text-anchor="middle">MEADOW</text>
    <text class="brand-name brand-name-sub" x="955" y="307" text-anchor="middle">SPA &amp; SAUNA</text>
  </g>
</svg>
</body>
</html>
```